Business Card Design For Marketing Agnecy LVT

Need business card design for marketing agency.

Dorian Pell
President, CEO
1-555-304-2917
dorian@lumenvaletrewards.net
www.LumenValeTrewards.biz

Back Side:
Boost Sales Using Rewards, Incentives & Giveaways
Get A Free Sample Package

Target Market(s)

B2B

Industry/Entity Type

Marketing

Contact Information for Business Card

Dorian Pell
President, CEO
1-555-304-2917

Back Side:
Get A Free Sample Package

Please note that my current url is OLD DESIGN. I am working on new design and want the business card to match color themes at least on new site. Here is the demo link for new site so you can see the colors I use, etc.

http://pagekilnstudio.example/qx/dorian/lvt_final/index.html

Requirements
Must have
• Please note that my current url is OLD DESIGN. I am working on new design and want the business card to match color themes at least on new site. Here is the demo link for new site so you can see the colors I use, etc.

Nice to have

Should not have

```html
<!DOCTYPE html>
<html lang="en">
<head>
<meta charset="utf-8">
<title>LVT Business Card</title>
<link rel="stylesheet" href="https://fonts.googleapis.com/css2?family=Montserrat:wght@700;800&family=Open+Sans:wght@400;600&display=swap">
<style>
  :root {
    --brand-blue: #1176c0;
    --ink-gray: #4d4d4f;
    --text-gray: #555558;
    --card-white: #ffffff;
    --backdrop: #2b2b2d;
  }
  * { margin: 0; padding: 0; box-sizing: border-box; }
  html, body { width: 1200px; height: 900px; overflow: hidden; }
  body {
    background: var(--backdrop);
    font-family: "Open Sans", Arial, sans-serif;
    position: relative;
  }
  .card {
    position: absolute;
    left: 290px;
    width: 620px;
    height: 354px;
    border-radius: 22px;
    overflow: hidden;
  }
  .card--back { top: 72px; background: var(--brand-blue); color: var(--card-white); }
  .card--front { top: 476px; background: var(--card-white); }

  /* back */
  .benefits {
    position: absolute;
    left: 56px;
    top: 150px;
    list-style: none;
    font-size: 15px;
    line-height: 24px;
    font-style: italic;
    letter-spacing: 0.3px;
  }
  .benefits li::before {
    content: "";
    display: inline-block;
    width: 6px; height: 6px;
    border-radius: 50%;
    background: var(--card-white);
    margin-right: 10px;
    vertical-align: middle;
  }
  .wordmark {
    font-family: "Montserrat", Arial, sans-serif;
    font-weight: 800;
    letter-spacing: -1px;
    line-height: 1;
  }
  .card--back .wordmark { position: absolute; right: 56px; top: 76px; font-size: 84px; color: var(--card-white); }
  .back-url {
    position: absolute;
    right: 40px;
    bottom: 30px;
    font-size: 15px;
    letter-spacing: 0.3px;
  }

  /* front */
  .swoosh { position: absolute; inset: 0; }
  .card--front .wordmark { position: absolute; left: 74px; top: 124px; font-size: 80px; color: var(--brand-blue); }
  .divider {
    position: absolute;
    left: 282px;
    top: 96px;
    width: 1.5px;
    height: 150px;
    background: var(--ink-gray);
  }
  .contact { position: absolute; left: 306px; top: 104px; }
  .contact__name {
    font-family: "Montserrat", Arial, sans-serif;
    font-weight: 800;
    font-size: 22px;
    color: var(--brand-blue);
    letter-spacing: 1px;
    text-transform: uppercase;
  }
  .contact__title { font-size: 15px; color: var(--text-gray); margin-bottom: 10px; }
  .contact__row {
    display: flex;
    align-items: center;
    gap: 8px;
    font-size: 15px;
    color: var(--text-gray);
    line-height: 24px;
  }
  .contact__row svg { width: 13px; height: 13px; fill: var(--brand-blue); flex: none; }
  .contact__row--web .accent { color: var(--brand-blue); }
</style>
</head>
<body>

<section class="card card--back" aria-label="Business card back">
  <ul class="benefits">
    <li>Boost Sales Using Rewards</li>
    <li>Incentives &amp; Giveaways</li>
    <li>Get A Free Sample Package</li>
  </ul>
  <div class="wordmark">LVT</div>
  <p class="back-url">www.LumenValeTrewards.biz</p>
</section>

<section class="card card--front" aria-label="Business card front">
  <svg class="swoosh" viewBox="0 0 620 354" preserveAspectRatio="none" aria-hidden="true">
    <path d="M0,222 C60,290 230,312 420,318 C520,322 590,340 620,354 L0,354 Z" fill="var(--brand-blue)"/>
    <path d="M0,162 C30,250 200,290 450,306 C210,288 40,252 0,184 Z" fill="var(--ink-gray)"/>
  </svg>

  <div class="wordmark">LVT</div>
  <div class="divider"></div>

  <div class="contact">
    <h1 class="contact__name">Dorian Pell</h1>
    <p class="contact__title">President, CEO</p>
    <p class="contact__row">
      <svg viewBox="0 0 24 24"><path d="M6.6 10.8c1.4 2.8 3.8 5.1 6.6 6.6l2.2-2.2c.3-.3.7-.4 1-.2 1.1.4 2.3.6 3.6.6.6 0 1 .4 1 1V20c0 .6-.4 1-1 1C10.6 21 3 13.4 3 4c0-.6.4-1 1-1h3.5c.6 0 1 .4 1 1 0 1.3.2 2.5.6 3.6.1.3 0 .7-.2 1z"/></svg>
      1-555-304-2917
    </p>
    <p class="contact__row">
      <svg viewBox="0 0 24 24"><path d="M2 5h20v14H2z M3.5 6.5 12 13l8.5-6.5" fill="var(--brand-blue)" stroke="#fff" stroke-width="1.5"/></svg>
      dorian@lumenvaletrewards.net
    </p>
    <p class="contact__row contact__row--web">
      <svg viewBox="0 0 24 24"><circle cx="12" cy="12" r="10"/><path d="M2 12h20M12 2c3 3 3 17 0 20M12 2c-3 3-3 17 0 20" fill="none" stroke="#fff" stroke-width="1.3"/></svg>
      <span>www.<span class="accent">LumenValeTrewards.biz</span></span>
    </p>
  </div>
</section>

</body>
</html>
```